Lantern Lane Town Footpath Chronicle Trek

We are launching a different kind of city historical walking tour company with a slightly darker approach using historical but real stories that have long been forgotten from living memory.
Our tour is going to contain a lot of very thoroughly researched stories ranging from 50 to 150 years past that takes the customer into the actual-real life past of the city streets.  Stories that may contains some dark undertones and stories with a twist or that seem eccentric to us now but were entirely normal back in olden times - minus the dry historical facts that most tours engage in..
Our tours are going to run both day and night and will incorporate real history / real Lantern Lane, so some of the stories will be quite serious (e.g.- there are actual murders from 100 years ago, baffling court cases, even a bit of poetry written by murderers, suicides, love triangles, you name it.  We are aiming for a mystery/history theme and are aiming to attract tourists who are interested in getting a different kind of history.

We're not going for scares and even though we expect people to enjoy our tours;  we're not aiming at light fun and frivolity.  I guess if you wanted to give us a tv rating we'd be aiming at M to MA15+.
If I was to give you another analogy using the literature world.  Think Edwin Harrowgates Nocturno rather than the Moonrise Saga of movies.  Or Clara Wendham's Gravemoor rather than the Pickwells.  Even Crown of Embers rather than a soap opera.
Our stories are being carefully crafted and are packed with unexpected twists, turns & revelations whilst remaining all 100% true.  We have approx 15-20 stories for each tour and we're designing them in a way that each story will trigger a different range of emotions in the listeners on a regular basis.  We're being very careful to keep it fresh for each story so that it will next to impossible for our guests to zone out!  I personally can't stand going on a tour where mildly interesting facts are read out.  We like deep, rich stories rather than pop entertainment.
We want the website to generate a feeling/atmosphere for our product that draws the right crowd to our tours as well as making it easy to make a booking.  Basic features to include:-
Home Page
Bookings Page
Integration with a booking system will be required here via use of plugin code.
Private Functions Page
We are hoping to integrate with a booking system via use of plugin code.  If not, then a simple form enquiry type input e.g.- name, emails, subject, contact, details, preferred date/time, etc).
About Us Page :-
Dark; a euphemism for the unknown or the forgotten.  Think dark ages, dark matter, dark energy; things where knowledge is uncertain or unknown are often termed dark.   Lantern lane brings back the hidden past, the forgotten past, the past that may not want to be remembered……but these are real stories....real stories that come from the streets around you.

Some of these stories may be tales of dark things.....some may simply be a charming reminder of days gone by…..regardless these stories are compelling reminders of the amazing times that precede us…..and the forgotten people of yesteryear finally get a chance to have their story told to a fresh audience.  Through you, the people of yesterday get to live again.  Will you like what you hear?

Contact Us page:-
•	A form input type page.
•	Include space for our phone number
•	Include space for our email address
Other Items:-
Social Media Links; we will be looking for social media icons to link to our social media pages to Chatterbook, Snapfolio, Chirplet.
Subscription; we want to also capture an input email address box for site visitors.  We will be launching a weekly Lantern Lane podcast / email newsetter; with a weekly Lantern Lane from a different place in the world and we want some way for people to subscribe.

Updates
Project Deadline Extended
Reason: A few additional photos have been uploaded.  Feel free to utilize if helpful.  Our stories range from the 1800s to 1950s in an era with beautiful old Victorian buildings.  I'm putting through the extension just to give some more time to see if this gives any more ideas and inspiration.  Thank you for all the great submissions.

Target Market(s)
Tourists that want to hear a darker version of the city they are visiting. Stories that other tour companies would not even think of covering. The real history of the events that ordinary people lived through that didn't necessarily make the history books. All stories are true; as per project description.
Industry/Entity Type
Tourism
Coding
Coded - Design and coding required
Number of Pages Required
5+ page
Colors
Designer to choose colors to be used in the design.
Look and feel

```html
<!DOCTYPE html>
<html lang="en">
<head>
<meta charset="utf-8">
<title>Lantern Lane</title>
<link href="https://fonts.googleapis.com/css2?family=Open+Sans:wght@400;600;700&family=Roboto+Slab:wght@400;700&display=swap" rel="stylesheet">
<style>
:root{
  --stage:#ececec;
  --paper:#ffffff;
  --sand:#e8e5df;
  --ink:#2b2b2b;
  --muted:#8a8580;
  --red:#e0474c;
  --red-dark:#c8363b;
  --nav:#2a2624;
  --bar:#b9b1a8;
  --gold:#f2c200;
  --line:#dcd8d2;
}
*{box-sizing:border-box;margin:0;padding:0}
html,body{width:1200px;height:1200px;overflow:hidden;background:var(--stage);font-family:"Open Sans",sans-serif;color:var(--ink)}
.page{position:absolute;left:390px;top:15px;width:525px;height:1462px;transform:scale(.8);transform-origin:0 0;background:var(--sand);box-shadow:0 0 24px rgba(0,0,0,.25);overflow:hidden}
.header{height:33px;background:var(--paper);position:relative}
.brand{position:absolute;left:20px;top:11px;display:flex;align-items:center;gap:4px;font-size:7px;font-weight:700;color:var(--ink);letter-spacing:.3px}
.brand i{width:9px;height:9px;background:var(--red);display:block}
.support{position:absolute;left:262px;top:9px;display:flex;gap:4px;align-items:center;font-size:4px;line-height:6px;color:var(--ink)}
.support .dot{width:13px;height:13px;border-radius:50%;background:var(--ink);display:flex;align-items:center;justify-content:center}
.search{position:absolute;left:328px;top:8px;width:103px;height:15px;border:1px solid var(--line);border-radius:8px;font-size:4.5px;color:var(--muted);padding:4px 6px}
.search svg{position:absolute;right:5px;top:4px}
.login{position:absolute;right:20px;top:11px;font-size:6.5px}
.nav{height:16px;background:linear-gradient(#4a4542,var(--nav));display:flex;gap:8px;padding-left:20px;align-items:center;font-size:4.6px;font-weight:700;color:#fff}
.hero{position:relative;height:316px}
.hero-photo{position:absolute;inset:0;background:linear-gradient(180deg,#3f6aa8 0%,#6c8fc0 10%,#a86a2e 30%,#8a4f1d 55%,#b77a36 80%,#d9a24a 100%)}
.hero .arrow{position:absolute;top:174px;width:10px;height:10px;border:1px solid rgba(255,255,255,.7);border-radius:50%}
.finder{position:absolute;left:20px;top:211px;width:485px;height:72px;background:var(--paper);display:grid;grid-template-columns:121px 120px 120px 124px;font-size:4.5px;color:var(--ink)}
.finder>div{padding:7px 6px;border-right:1px solid var(--line)}
.finder>div:last-child{border:0}
.finder h4{font-size:6px;font-weight:400;margin-bottom:8px}
.finder h4 b{font-weight:700}
.opts{display:grid;grid-template-columns:1fr 1fr;row-gap:6px}
.opts span::before{content:"";display:inline-block;width:5px;height:5px;border:1px solid #bbb;border-radius:50%;margin-right:5px;vertical-align:middle}
.field{height:14px;border:1px solid var(--line);border-radius:7px;margin-top:4px;padding:4px 4px;color:var(--muted)}
.pair{display:flex;gap:4px}.pair>div{flex:1}
.go{position:absolute;left:222px;top:269px;width:82px;height:13px;border-radius:7px;background:linear-gradient(#ef6a6e,var(--red-dark));color:#fff;font-size:4.2px;font-weight:700;text-align:center;line-height:13px}
h2{font-family:"Roboto Slab",serif;font-size:10.5px;font-weight:400;position:absolute;left:20px}
.grid{position:absolute;left:20px;display:grid;grid-template-columns:repeat(4,115px);column-gap:9px}
.card{background:var(--paper);box-shadow:0 1px 2px rgba(0,0,0,.12)}
.photo{height:76px}
.t1{background:linear-gradient(#86a6c9,#a78552 55%,#6d5a3a)}
.t2{background:linear-gradient(#8fb0d1,#b2593a 40%,#8c3e28)}
.t3{background:linear-gradient(#4a7fc4,#a38f6f 50%,#7a6b55)}
.t4{background:linear-gradient(#5c84b6,#9a5a31 40%,#6f3f22)}
.t5{background:linear-gradient(#6f5a3c,#c07a3a 50%,#4a2e1b)}
.t6{background:linear-gradient(#b8c6d3,#6f6a5c 50%,#4d5a3a)}
.offer p{font-size:5.5px;padding:7px 6px;border-bottom:1px solid var(--line);white-space:nowrap;overflow:hidden}
.pill{display:block;margin:7px auto 10px;width:fit-content;padding:0 8px;height:10px;line-height:10px;border-radius:5px;background:linear-gradient(#ef6a6e,var(--red-dark));color:#fff;font-size:4px;font-weight:700}
.dest{position:relative;height:140px}
.dest .row{display:flex;justify-content:space-between;align-items:center;padding:6px 6px 0;font-size:5.8px;font-weight:600;white-space:nowrap}
.dest .row .pill{margin:0;font-size:3.8px}
.dest .row .pill.grey{background:#c9c4bd}
.dest small{display:block;font-size:4px;color:var(--muted);padding:5px 6px}
.prices{position:absolute;left:-2px;right:-2px;bottom:5px;height:22px;background:var(--bar);display:flex;align-items:center;justify-content:space-around;color:#fff;font-size:6.5px}
.prices.hot{background:var(--gold);color:#333}
.prices em{font-style:normal;font-size:3.4px;display:block;text-align:center}
.badge{position:absolute;right:0;top:0;background:var(--gold);color:#fff;font-size:4.5px;padding:3px 3px}
.rule{position:absolute;left:20px;right:20px;top:1080px;border-top:1px solid var(--line)}
.feature{height:84px;padding:8px 6px}
.feature h3{font-family:"Roboto Slab",serif;font-size:6px;font-weight:700;margin-bottom:10px}
.feature p{font-size:4.3px;line-height:7.6px;color:#6f6a64}
.footer{position:absolute;left:0;right:0;top:1357px;bottom:0;background:var(--paper);font-size:4.6px;color:#555}
.fcol{position:absolute;top:13px}
.fcol h5{font-family:"Roboto Slab",serif;font-size:6.5px;font-weight:400;color:#8a8580;margin-bottom:8px}
.fcol li{list-style:none;line-height:9px}
.fcol li::before{content:"";display:inline-block;width:2px;height:2px;background:#555;margin-right:4px;vertical-align:middle}
.socials{display:flex;gap:3px}.socials i{width:11px;height:11px;border-radius:50%;background:#bdb7b0;display:block}
.sub{display:flex}.sub span{width:82px;height:13px;border:1px solid var(--line);padding:3px 4px;color:var(--muted)}
.sub b{height:13px;width:33px;background:var(--red);color:#fff;font-size:4px;text-align:center;line-height:13px}
.copy{position:absolute;left:20px;right:20px;bottom:10px;border-top:1px solid var(--line);padding-top:6px;display:flex;justify-content:space-between;font-size:4.2px;color:#888}
.copy nav{display:flex;gap:10px}
</style>
</head>
<body>
<div class="page">
  <header class="header">
    <div class="brand"><i></i>Lantern Lane</div>
    <div class="support"><span class="dot"><svg width="7" height="7" viewBox="0 0 24 24"><path fill="#e0474c" d="M6.6 10.8a15 15 0 0 0 6.6 6.6l2.2-2.2c.3-.3.7-.4 1-.2 1.1.4 2.3.6 3.6.6.6 0 1 .4 1 1V20c0 .6-.4 1-1 1A17 17 0 0 1 3 4c0-.6.4-1 1-1h3.5c.6 0 1 .4 1 1 0 1.3.2 2.5.6 3.6.1.3 0 .7-.2 1z"/></svg></span><span>Bookings<br>555-210-4471</span></div>
    <div class="search">Search our forgotten stories<svg width="6" height="6" viewBox="0 0 10 10"><circle cx="4" cy="4" r="3" fill="none" stroke="#999"/><path d="M6 6l3 3" stroke="#999"/></svg></div>
    <div class="login">Login</div>
  </header>
  <nav class="nav"><span>HOME</span><span>DAY TOURS</span><span>NIGHT TOURS</span><span>BOOKINGS</span><span>PRIVATE FUNCTIONS</span><span>STORIES</span><span>PODCAST</span><span>ABOUT US</span><span>CONTACT</span></nav>
  <section class="hero">
    <div class="hero-photo" role="img" aria-label="Old weathered stone buildings at dusk on a historic city street"></div>
    <span class="arrow" style="left:5px"></span><span class="arrow" style="right:5px"></span>
    <form class="finder">
      <div><h4><b>01</b> What?</h4><div class="opts"><span>Day Tour</span><span>Night Tour</span><span>Private Event</span><span>Group Walk</span><span>Gift Voucher</span><span>Live Podcast</span></div></div>
      <div><h4><b>02</b> Where?</h4>Starting point<div class="field">City, street or story name</div></div>
      <div><h4><b>03</b> When?</h4><div class="pair"><div>Tour date<div class="field"></div></div><div>Start time<div class="field"></div></div></div></div>
      <div><h4><b>04</b> Who?</h4><div class="pair"><div>Adults<div class="field"></div></div><div>Teens 15+<div class="field"></div></div><div>Groups<div class="field"></div></div></div></div>
    </form>
    <div class="go">CHECK AVAILABILITY</div>
  </section>

  <h2 style="top:384px">Uncover our latest tours</h2>
  <div class="grid" style="top:416px">
    <div class="card offer"><div class="photo t1" role="img" aria-label="Victorian terrace lit by gas lamps"></div><p>Night walk: the 1908 murders</p><span class="pill">BOOK THIS TOUR</span></div>
    <div class="card offer"><div class="photo t2" role="img" aria-label="Red brick courthouse walls"></div><p>Baffling court cases of 1890</p><span class="pill">MORE INFO</span></div>
    <div class="card offer"><div class="photo t3" role="img" aria-label="Crumbling stone laneway"></div><p>Love triangles &amp; lost letters</p><span class="pill">BOOK THIS TOUR</span></div>
    <div class="card offer"><div class="photo t4" role="img" aria-label="Arched gateway at twilight"></div><p>Private functions for groups</p><span class="pill">MORE INFO</span></div>
  </div>

  <h2 style="top:579px">Streets with forgotten stories</h2>
  <div class="grid" style="top:611px;row-gap:11px">
    <div class="card dest"><div class="photo t6" role="img" aria-label="Old chapel among trees"></div><div class="row">Chapel Row<span class="pill">VIEW TOUR</span></div><small>18 Stories</small><div class="prices"><span>☀</span><span><em>day</em>$ 35</span><span>☾</span><span><em>night</em>$ 45</span></div></div>
    <div class="card dest"><div class="photo t5" role="img" aria-label="Dim arcade of carved stone"></div><div class="row">Gaslight Arcade<span class="pill">VIEW TOUR</span></div><small>16 Stories</small><div class="prices"><span>☀</span><span><em>day</em>$ 35</span><span>☾</span><span><em>night</em>$ 45</span></div></div>
    <div class="card dest"><div class="photo t1" role="img" aria-label="Victorian terrace facade"></div><div class="row">Harbour Street<span class="pill">VIEW TOUR</span></div><small>20 Stories</small><div class="prices"><span>☀</span><span><em>day</em>$ 35</span><span>☾</span><span><em>night</em>$ 45</span></div></div>
    <div class="card dest"><div class="photo t2" role="img" aria-label="Red brick gaol walls"></div><div class="row">Old Gaol Hill<span class="pill">VIEW TOUR</span></div><small>15 Stories</small><div class="prices"><span>☀</span><span><em>day</em>$ 35</span><span>☾</span><span><em>night</em>$ 45</span></div></div>

    <div class="card dest"><div class="photo t6" role="img" aria-label="Churchyard gate and trees"></div><div class="row">Graveyard Lane<span class="pill">VIEW TOUR</span></div><small>17 Stories</small><div class="prices"><span>☀</span><span><em>day</em>$ 35</span><span>☾</span><span><em>night</em>$ 45</span></div></div>
    <div class="card dest"><div class="photo t3" role="img" aria-label="Weathered stone market hall"></div><span class="badge">-20%</span><div class="row">Market Square<span class="pill grey">VIEW TOUR</span></div><small>19 Stories</small><div class="prices hot"><span>☀</span><span><em>day</em>$ 28</span><span>☾</span><span><em>night</em>$ 36</span></div></div>
    <div class="card dest"><div class="photo t4" role="img" aria-label="Arched gateway at dusk"></div><div class="row">Tanners Gate<span class="pill">VIEW TOUR</span></div><small>15 Stories</small><div class="prices"><span>☀</span><span><em>day</em>$ 35</span><span>☾</span><span><em>night</em>$ 45</span></div></div>
    <div class="card dest"><div class="photo t5" role="img" aria-label="Carved stone hall interior"></div><div class="row">Bridewell Walk<span class="pill">VIEW TOUR</span></div><small>16 Stories</small><div class="prices"><span>☀</span><span><em>day</em>$ 35</span><span>☾</span><span><em>night</em>$ 45</span></div></div>

    <div class="card dest"><div class="photo t1" role="img" aria-label="Old townhouse facade"></div><div class="row">Orchard Place<span class="pill">VIEW TOUR</span></div><small>18 Stories</small><div class="prices"><span>☀</span><span><em>day</em>$ 35</span><span>☾</span><span><em>night</em>$ 45</span></div></div>
    <div class="card dest"><div class="photo t2" role="img" aria-label="Red brick warehouse walls"></div><div class="row">Quay Street<span class="pill">VIEW TOUR</span></div><small>17 Stories</small><div class="prices"><span>☀</span><span><em>day</em>$ 35</span><span>☾</span><span><em>night</em>$ 45</span></div></div>
    <div class="card dest"><div class="photo t3" role="img" aria-label="Stone courthouse steps"></div><div class="row">Assize Court<span class="pill">VIEW TOUR</span></div><small>20 Stories</small><div class="prices"><span>☀</span><span><em>day</em>$ 35</span><span>☾</span><span><em>night</em>$ 45</span></div></div>
    <div class="card dest"><div class="photo t4" role="img" aria-label="Old city wall tower"></div><div class="row">Wall Road<span class="pill">VIEW TOUR</span></div><small>15 Stories</small><div class="prices"><span>☀</span><span><em>day</em>$ 35</span><span>☾</span><span><em>night</em>$ 45</span></div></div>
  </div>

  <div class="rule"></div>

  <div class="grid" style="top:1105px;row-gap:8px">
    <div class="card feature"><h3>All Stories True</h3><p>Every tale is thoroughly researched from archives, court records and papers. No invention, no scares, just real lives.</p></div>
    <div class="card feature"><h3>Forgotten Voices</h3><p>Stories from 50 to 150 years past that slipped out of living memory, told again on the very streets they happened.</p></div>
    <div class="card feature"><h3>Twists &amp; Revelations</h3><p>15 to 20 stories per tour, each crafted to stir a new emotion, so you will never zone out on dry facts.</p></div>
    <div class="card feature"><h3>Day &amp; Night Walks</h3><p>Walk by daylight or by lantern after dark. Tours suit guests aged 15+ given some serious themes.</p></div>
    <div class="card feature"><h3>Private Functions</h3><p>Book a tour just for your group, party or company. Tell us your date, time and numbers and we will shape the night around you.</p></div>
    <div class="card feature"><h3>Secure Booking</h3><p>Our booking system is secure and your card and personal details are encrypted. Reserve your walk in a few quick steps.</p></div>
    <div class="card feature"><h3>Weekly Podcast</h3><p>Each week a new Lantern Lane story from a different place in the world, sent straight to your inbox or player.</p></div>
    <div class="card feature"><h3>Any Questions?</h3><p>Call us on 555-210-4471 for advice on the right tour or <b>send us a message</b> with your booking query.</p></div>
  </div>

  <footer class="footer">
    <div class="fcol" style="left:20px"><div class="brand" style="position:static;margin-bottom:10px"><i></i>Lantern Lane</div>
      <p style="line-height:8px">Millbrook Row, Ashford Vale<br><b>P:</b> Bookings: 555-210-4471<br><b>E:</b> hello@lanternlane.example</p></div>
    <div class="fcol" style="left:143px"><h5>Customer support</h5><ul><li>Faq</li><li>How do I book a tour?</li><li>Private functions</li><li>Gift vouchers</li></ul></div>
    <div class="fcol" style="left:267px"><h5>Follow us</h5><div class="socials"><i aria-label="Chatterbook"></i><i aria-label="Snapfolio"></i><i aria-label="Chirplet"></i></div></div>
    <div class="fcol" style="left:390px"><h5>Get our weekly podcast</h5><div class="sub"><span>Enter your email here</span><b>SUBSCRIBE</b></div></div>
    <div class="copy"><span>Copyright 2017 Lantern Lane. All rights reserved</span><nav><span>About us</span><span>Contact</span><span>Bookings</span><span>Private functions</span><span>FAQ</span><span>Podcast</span><span>Terms &amp; Conditions</span><span>Privacy statement</span></nav></div>
  </footer>
</div>
</body>
</html>
```